依頼詳細
※1ページのデザインでお願いいたします。
※通常のホームページのようにナビゲーションは必要ありません。
※高級感を出したイメージをお願いいたします。

■色
色はブラウン・グリーン・オレンジ・ベージュ等。
グリーンは、サンプルサイトのように緑の葉やフローラルな感じで演出をお願いいたします。

■配置
上部左側にロゴ、右側に営業時間等、電話番号の表示
(時間、電話番号はこちらで入力いたします)

メイン部分に、添付した料金(レイアウトを変更してもかまいません)
写真配置は、サンプルサイトのように大きさをランダムにお願いいたします。
写真はまだありませんので、ダミーを入れてください。

下にはコピーライトとロゴ表示をお願いいたします。

■納品
フォトショップ形式で納品をお願いいたします。
コーディングは必要ありません。

■サンプルサイト
http://atelierwisteo.com/

どうぞよろしくお願いいたします。
1ページ
茶系、緑系
• フォトショップ形式 (.psd)

派手すぎず、地味すぎず、ほぼ希望通りのデザインに仕上げていただきました。
見せ方など全体的にまとまっていてバランスがとれていると思います。

この度は、多数のご提案ありがとうございました。
とても一生懸命にデザインされ、選ぶのにとても悩みました。

また機会がございましたらよろしくお願いいたします。

```html
<!DOCTYPE html>
<html lang="ja">
<head>
<meta charset="utf-8">
<title>Fiorena ヘアサロン</title>
<link rel="stylesheet" href="https://fonts.googleapis.com/css2?family=Cormorant+Garamond:wght@500;600&family=Noto+Serif+JP:wght@400;600&family=Noto+Sans+JP:wght@400;500&display=swap">
<style>
:root{
  --brown:#5a4230;
  --brown-soft:#8a6a4c;
  --green:#7aa43a;
  --green-dark:#4f7a22;
  --orange:#e07a1f;
  --beige:#efe3cf;
  --beige-bar:#e6d6bb;
  --wood:#d9cdbb;
  --ink:#3b3129;
  --night:#1f1f22;
  --white:#ffffff;
}
*{margin:0;padding:0;box-sizing:border-box}
html,body{width:1200px;height:2484px;overflow:hidden}
body{background:var(--white);font-family:"Noto Sans JP",sans-serif;color:var(--ink);position:relative}

.site-header{position:absolute;top:0;left:0;width:1200px;height:108px;display:flex;justify-content:space-between;align-items:center;padding:0 40px}
.brand{font-family:"Cormorant Garamond",serif;font-weight:600;font-size:54px;color:var(--brown);letter-spacing:1px;display:flex;align-items:center;gap:14px}
.brand-dot{width:14px;height:14px;border-radius:50%;background:var(--green)}
.contact{text-align:right;color:var(--brown)}
.contact .tagline{font-size:13px}
.contact .tel{font-family:"Noto Serif JP",serif;font-size:30px;font-weight:600;letter-spacing:1px;line-height:1.2}
.contact .hours{font-size:12px}

.gallery{position:absolute;top:108px;left:0;width:1200px;height:412px}
.gallery .photo{position:absolute}
.p-salon{left:0;top:0;width:620px;height:412px;background:linear-gradient(135deg,#b58a5e,#e7d2b2 55%,#a8704a)}
.p-stylist{left:620px;top:0;width:340px;height:252px;background:linear-gradient(160deg,#f1ebe2,#c9a88a 60%,#8a6247)}
.p-tools{left:960px;top:0;width:240px;height:252px;background:linear-gradient(160deg,#e4e2df,#9a948e)}
.p-wash{left:620px;top:252px;width:240px;height:160px;background:linear-gradient(160deg,#dcdcda,#7f7b77)}
.p-curl{left:860px;top:252px;width:340px;height:160px;background:linear-gradient(160deg,#d5b89a,#7d5436)}

.menu-area{position:absolute;top:520px;left:0;width:1200px;height:1080px;background:linear-gradient(90deg,#d8ccba,#e6ddcf 30%,#d3c6b2 60%,#e2d8c8)}
.vine{position:absolute;background:radial-gradient(ellipse at center,rgba(108,160,52,.75),rgba(108,160,52,0) 70%)}
.vine-tl{left:40px;top:20px;width:300px;height:140px}
.vine-tr{right:40px;top:20px;width:300px;height:140px}
.vine-bl{left:40px;bottom:20px;width:260px;height:140px}
.vine-br{right:40px;bottom:30px;width:260px;height:140px}

.menu-card{position:absolute;left:112px;top:60px;width:976px;height:960px;background:rgba(255,255,255,.94);padding:40px 48px}
.menu-title{text-align:center;font-family:"Cormorant Garamond",serif;font-size:40px;letter-spacing:4px;color:var(--brown)}
.menu-title::after{content:"";display:block;width:140px;height:1px;background:var(--brown-soft);margin:6px auto 0}
.menu-cols{display:flex;gap:40px;margin-top:28px}
.menu-col{flex:1}
.menu-sec{margin-bottom:22px}
.sec-head{display:flex;align-items:center;gap:10px;background:linear-gradient(90deg,var(--beige-bar),var(--beige));height:30px;padding:0 10px;font-family:"Noto Serif JP",serif;font-size:15px;color:var(--brown)}
.sec-head small{font-size:10px;color:var(--brown-soft)}
.sec-note{text-align:right;font-size:10px;color:var(--brown-soft);margin:4px 0 6px}
.item{display:flex;justify-content:space-between;font-size:14px;padding:4px 6px;color:var(--ink)}
.item .sub{font-size:10px;color:var(--brown-soft);display:block}
.item .price{font-family:"Noto Serif JP",serif;white-space:nowrap}

.map-area{position:absolute;top:1600px;left:0;width:1200px;height:800px;background:linear-gradient(180deg,#2a2a2e,#3d3a37 50%,#1b1b1d)}
.map-title{position:absolute;top:60px;width:100%;text-align:center;font-family:"Cormorant Garamond",serif;font-size:44px;letter-spacing:6px;color:var(--white)}
.map-box{position:absolute;left:260px;top:128px;width:680px;height:272px;border:1px solid rgba(255,255,255,.7);background:linear-gradient(135deg,#33322f,#55504a)}
.shop-info{position:absolute;left:310px;top:440px;color:var(--white)}
.shop-name{font-family:"Cormorant Garamond",serif;font-size:44px;letter-spacing:6px}
.shop-addr{font-size:16px;margin-top:6px;letter-spacing:2px}
.shop-tel{font-family:"Noto Serif JP",serif;font-size:22px;letter-spacing:3px;margin-top:4px}
.shop-note{font-family:"Noto Serif JP",serif;font-size:22px;letter-spacing:8px;margin-top:36px}

.site-footer{position:absolute;top:2400px;left:0;width:1200px;height:84px;display:flex;align-items:center;justify-content:center;font-size:12px;color:#999}
</style>
</head>
<body>

<header class="site-header">
  <div class="brand"><span class="brand-dot"></span>Fiorena</div>
  <div class="contact">
    <p class="tagline">鎌倉の完全予約制ヘアサロン</p>
    <p class="tel">TEL.000-000-0000</p>
    <p class="hours">営業時間 10:00〜19:00 / 定休日 火曜</p>
  </div>
</header>

<section class="gallery">
  <div class="photo p-salon" role="img" aria-label="サロン店内の写真"></div>
  <div class="photo p-stylist" role="img" aria-label="スタイリング中の写真"></div>
  <div class="photo p-tools" role="img" aria-label="ヘアケア道具の写真"></div>
  <div class="photo p-wash" role="img" aria-label="シャンプー台の写真"></div>
  <div class="photo p-curl" role="img" aria-label="ヘアスタイルの写真"></div>
</section>

<section class="menu-area">
  <div class="vine vine-tl" role="img" aria-label="緑の葉のつる飾り"></div>
  <div class="vine vine-tr" role="img" aria-label="緑の葉のつる飾り"></div>
  <div class="vine vine-bl" role="img" aria-label="緑の葉のつる飾り"></div>
  <div class="vine vine-br" role="img" aria-label="緑の葉のつる飾り"></div>

  <div class="menu-card">
    <h2 class="menu-title">MENU</h2>
    <div class="menu-cols">
      <div class="menu-col">
        <div class="menu-sec">
          <div class="sec-head"><svg width="14" height="14" viewBox="0 0 14 14"><path d="M2 12C2 5 7 2 12 2C12 8 8 12 2 12Z" fill="#7aa43a"/></svg>カット <small>シャンプー・ブロー込</small></div>
          <div class="item"><span>一般カット</span><span class="price">4,000 円</span></div>
        </div>
        <div class="menu-sec">
          <div class="sec-head"><svg width="14" height="14" viewBox="0 0 14 14"><path d="M2 12C2 5 7 2 12 2C12 8 8 12 2 12Z" fill="#7aa43a"/></svg>デザインカラー <small>シャンプー・ブロー込</small></div>
          <p class="sec-note">ロング料金+500円</p>
          <div class="item"><span>Re:ナチュラルカラー<span class="sub">白髪染め・ベーシック</span></span><span class="price">3,500 円</span></div>
          <div class="item"><span>ハイライト</span><span class="price">3,000 円</span></div>
          <div class="item"><span>ヘナ（100%天然植物）</span><span class="price">4,000 円</span></div>
          <div class="item"><span>マニキュア <small>髪艶トリートメント付</small></span><span class="price">3,000 円</span></div>
        </div>
        <div class="menu-sec">
          <div class="sec-head"><svg width="14" height="14" viewBox="0 0 14 14"><path d="M2 12C2 5 7 2 12 2C12 8 8 12 2 12Z" fill="#7aa43a"/></svg>パーマ <small>シャンプー・ブロー込</small></div>
          <p class="sec-note">ロング料金+500円</p>
          <div class="item"><span>ベーシックパーマ</span><span class="price">3,500 円</span></div>
          <div class="item"><span>プラチナムパーマ<span class="sub">髪質改善トリートメント付</span></span><span class="price">5,500 円</span></div>
          <div class="item"><span>デジタルパーマ</span><span class="price">5,000 円</span></div>
          <div class="item"><span>ポイントパーマ<span class="sub">前髪・毛先など部分施術</span></span><span class="price">4,500 円</span></div>
        </div>
        <div class="menu-sec">
          <div class="sec-head"><svg width="14" height="14" viewBox="0 0 14 14"><path d="M2 12C2 5 7 2 12 2C12 8 8 12 2 12Z" fill="#7aa43a"/></svg>セット</div>
          <div class="item"><span>アップセット</span><span class="price">1,000 円</span></div>
          <div class="item"><span>ブローセット</span><span class="price">1,000 円</span></div>
        </div>
      </div>

      <div class="menu-col">
        <div class="menu-sec">
          <div class="sec-head"><svg width="14" height="14" viewBox="0 0 14 14"><path d="M2 12C2 5 7 2 12 2C12 8 8 12 2 12Z" fill="#7aa43a"/></svg>ファッションカラー <small>シャンプー・ブロー込</small></div>
          <p class="sec-note">ロング料金+500円</p>
          <div class="item"><span>おしゃれ染め　ショート</span><span class="price">3,500 円</span></div>
          <div class="item"><span>　　　　　　　ミディアム</span><span class="price">4,000 円</span></div>
          <div class="item"><span>　　　　　　　ロング</span><span class="price">4,500 円</span></div>
          <div class="item"><span>全体脱色</span><span class="price">500 円</span></div>
        </div>
        <div class="menu-sec">
          <div class="sec-head"><svg width="14" height="14" viewBox="0 0 14 14"><path d="M2 12C2 5 7 2 12 2C12 8 8 12 2 12Z" fill="#7aa43a"/></svg>縮毛 <small>シャンプー・ブロー込</small></div>
          <p class="sec-note">ロング料金+500円</p>
          <div class="item"><span>スタンダード</span><span class="price">6,000 円</span></div>
          <div class="item"><span>プラチナム<span class="sub">髪質改善トリートメント付</span></span><span class="price">7,000 円</span></div>
          <div class="item"><span>プロポイント<span class="sub">前髪・顔まわりのみ</span></span><span class="price">8,000 円</span></div>
        </div>
        <div class="menu-sec">
          <div class="sec-head"><svg width="14" height="14" viewBox="0 0 14 14"><path d="M2 12C2 5 7 2 12 2C12 8 8 12 2 12Z" fill="#7aa43a"/></svg>トリートメント</div>
          <div class="item"><span>Re:トリートメント</span><span class="price">1,000 円</span></div>
          <div class="item"><span>プラチナムトリートメント<span class="sub">集中補修ケア</span></span><span class="price">1,500 円</span></div>
          <div class="item"><span>プロポイント<span class="sub">毛先集中ケア</span></span><span class="price">2,000 円</span></div>
        </div>
        <div class="menu-sec">
          <div class="sec-head"><svg width="14" height="14" viewBox="0 0 14 14"><path d="M2 12C2 5 7 2 12 2C12 8 8 12 2 12Z" fill="#7aa43a"/></svg>着付</div>
          <div class="item"><span>訪問</span><span class="price">3,500 円</span></div>
        </div>
        <div class="menu-sec">
          <div class="sec-head"><svg width="14" height="14" viewBox="0 0 14 14"><path d="M2 12C2 5 7 2 12 2C12 8 8 12 2 12Z" fill="#7aa43a"/></svg>セット</div>
          <div class="item"><span>ジェルネイル</span><span class="price">4,000 円</span></div>
        </div>
      </div>
    </div>
  </div>
</section>

<section class="map-area" role="img" aria-label="夜の街並みの背景写真">
  <h2 class="map-title">MAP</h2>
  <div class="map-box" role="img" aria-label="サロン周辺の道路地図"></div>
  <div class="shop-info">
    <p class="shop-name">Fiorena</p>
    <p class="shop-addr">鎌倉市小町1-2-3</p>
    <p class="shop-tel">TEL 000-00-0000</p>
    <p class="shop-note">プライベートルーム　完全予約制</p>
  </div>
</section>

<footer class="site-footer">© 2013 Fiorena All Rights Reserved.</footer>

</body>
</html>
```